Business Card for QRB Farmstock

Custom Business Card Brief:
1. We need two designs for this single client, QRB Farmstock LLC and both designs will end up with rounded corner printed cards that fit the PRINTLY.com design format for their special printing style.
2. My client needs two separate card designs since half of their target market is for farm owners in the Cattle and Beef world. The other half of their target market is working with Equine aka Horse farm owners.
3. The look for two card designs can be similar to ensure branding consistency but we will need some space sizing differences so the cards stand out differently in regards to how the services mentioned are laid out on the front of each card design.
4. Both card designs require the front of the card holding all of the great design work. The back of these 2-sided cards will remain white and can just have the contact information listed "again" on the back to match the contact information provided on the front.
5. Card Design 1 will be for Equine customers, Card Design 2 will be for his Cattle/Beef customers.
6. Card Design 1 (Equine) we are thinking we set aside 70% of the card to be dedicated to the Services listed section while the remaining 30% of the front of the card space will hold a smaller logo image space along with his name and contact information.
7. Card Design 2 (Cattle/Beef) we will need opposite of my last point. We want 70% of the card dedicated to a larger logo space and his contact information while the remaining 30% listing the services provided.
8. Card Design #1 - Equine - his Services space should include:
- Equine Mortality Services
- General Removal
- Cremation
- Transportation for Necropsy
9. Card Design #2 - Cattle/Beef - his Services space should include: General Livestock Services, Hauling, Order Buying, Dealing, Dead Stock Removal
10. Contact Information for both card designs:
- Gerald R. Fenwick (owner)
- QRB Farmstock LLC (company)
- 555-318-4692 (phone)
- info@qrbfarmstockservices.example (email)
- QRBFarmstockServices.example (website)
11. Additional Branding Details - The color codes aka pantone colors that are in the current logo file design:
- Blue Pantone 7686C
- Grey Pantone 422C
12. The font styles used in the logo:
- Nexa Bold
- Nexa Rust Slab Black Shadow
13. Back of both card designs, just list his contact information in larger size to stand out more on the white back:
- 555-318-4692 (phone)
Updates

Okay thanks for confirming that our final design files will be ready for the PRINTLY.com format. I noticed the 2nd place vertical card already had rounded corners but the horizontal design that was in 1st place still had sharp square corners. When using the PRINTLY.com format we will be rounding all of the corners of both cards for print. So we just wanted to make sure that both sets of files will be in a rounded design meeting their format sizing to ensure no content from your great designs gets cut off. Thank you again for your attention to detail. ~ Derek

Target Market(s)

Business to Business

Industry/Entity Type

Farming, Agriculture, Livestock

Contact Information for Business Card

Clients' logo, his contact info, and his different services on two similar final card designs.

Font styles to use
Other font styles liked:
• Look at the brief to see how his logo fonts are currently.

Requirements
Must have
• Two versions of the card, one for the Equine horse market, and one for the Cattle/Beef market of farming.
Nice to have
• Clean, sharp, concise.
Should not have
• No flashy or cartoony designs.

```html
<!DOCTYPE html>
<html lang="en">
<head>
<meta charset="utf-8">
<title>QRB Farmstock – Business Cards</title>
<link rel="stylesheet" href="https://fonts.googleapis.com/css2?family=Archivo:ital,wght@0,400;0,600;0,800;0,900;1,600;1,800&display=swap">
<style>
  :root {
    --navy: #0b2f55;
    --brand-blue: #1d4f91;
    --grey: #9ea2a2;
    --text-grey: #6b6e70;
    --stripe-grey: #c9cbcc;
    --card: #ffffff;
    --backdrop: #e6e8ea;
  }
  * { box-sizing: border-box; margin: 0; padding: 0; }
  html, body { width: 1200px; height: 900px; overflow: hidden; }
  body {
    background: var(--backdrop);
    font-family: "Archivo", Arial, sans-serif;
    position: relative;
  }
  .card {
    position: absolute;
    left: 250px;
    width: 700px;
    height: 400px;
    background: var(--card);
    border-radius: 34px;
    overflow: hidden;
    box-shadow: 0 6px 18px rgba(0,0,0,.12);
  }
  .card--equine { top: 34px; }
  .card--cattle { top: 466px; }
  .card__band { position: absolute; inset: 0; }

  .brand { position: absolute; left: 48px; top: 42px; width: 270px; }
  .brand__name {
    display: flex; align-items: center; gap: 10px;
    font-weight: 900; font-size: 34px; color: var(--brand-blue);
    letter-spacing: .5px; text-transform: uppercase; line-height: 1;
  }
  .brand__mark { width: 16px; height: 16px; border-radius: 50%; background: var(--brand-blue); flex: none; }
  .brand__place { margin-top: 8px; font-size: 12px; color: var(--grey); font-weight: 600; letter-spacing: 1px; }
  .brand__phone { margin-top: 6px; font-size: 28px; font-weight: 800; font-style: italic; color: var(--brand-blue); }

  .owner { position: absolute; left: 360px; top: 54px; right: 30px; }
  .owner__name { font-weight: 900; font-size: 27px; color: var(--navy); text-transform: uppercase; letter-spacing: .5px; }
  .owner__title { font-weight: 800; font-size: 17px; color: var(--text-grey); margin-top: 2px; }
  .owner__rule { height: 1.5px; background: var(--navy); margin: 12px 0 12px; width: 300px; }
  .contact { list-style: none; font-style: italic; font-weight: 600; font-size: 14.5px; color: var(--text-grey); }
  .contact li { display: flex; align-items: center; gap: 7px; margin-bottom: 5px; }
  .contact svg { width: 13px; height: 13px; flex: none; }

  .services__title {
    position: absolute; left: 48px; top: 198px;
    font-weight: 900; font-size: 22px; color: var(--navy); letter-spacing: .5px;
  }
  .rule { position: absolute; background: var(--navy); }
  .rule--services { left: 192px; right: 0; top: 213px; height: 1.5px; }
  .rule--lower { left: 290px; right: 0; top: 322px; height: 1.5px; }
  .rule--divider { left: 282px; top: 252px; width: 1.5px; height: 62px; transform: rotate(12deg); }
  .service-list {
    position: absolute; list-style: none;
    font-weight: 600; font-size: 15px; color: var(--text-grey); text-transform: uppercase; letter-spacing: .5px;
  }
  .service-list li { display: flex; align-items: center; gap: 10px; margin-bottom: 8px; }
  .service-list li::before { content: ""; width: 11px; height: 11px; border-radius: 50%; background: var(--navy); flex: none; }
  .service-list--left { left: 48px; top: 236px; }
  .service-list--right { left: 310px; top: 258px; }
</style>
</head>
<body>

<article class="card card--equine">
  <svg class="card__band" viewBox="0 0 700 400" preserveAspectRatio="none" aria-hidden="true">
    <path d="M0,362 L300,362 C330,362 345,368 360,376 L0,376 Z" fill="var(--stripe-grey)"/>
    <path d="M0,376 L300,376 C370,376 380,348 450,348 L700,348 L700,400 L0,400 Z" fill="var(--navy)"/>
  </svg>
  <div class="brand">
    <div class="brand__name"><span class="brand__mark"></span>QRB Farmstock</div>
    <div class="brand__place">Ridgeford, PA</div>
    <div class="brand__phone">555-318-4692</div>
  </div>
  <div class="owner">
    <div class="owner__name">Gerald R. Fenwick</div>
    <div class="owner__title">OWNER</div>
    <div class="owner__rule"></div>
    <ul class="contact">
      <li><svg viewBox="0 0 14 14"><rect x="1" y="3" width="12" height="8" fill="none" stroke="var(--navy)" stroke-width="1.3"/><path d="M1 3 L7 8 L13 3" fill="none" stroke="var(--navy)" stroke-width="1.3"/></svg>info@qrbfarmstockservices.example</li>
      <li><svg viewBox="0 0 14 14"><circle cx="7" cy="7" r="5.5" fill="none" stroke="var(--navy)" stroke-width="1.3"/><path d="M1.5 7 H12.5 M7 1.5 C4 5 4 9 7 12.5 M7 1.5 C10 5 10 9 7 12.5" fill="none" stroke="var(--navy)" stroke-width="1"/></svg>www.QRBFarmstockServices.example</li>
    </ul>
  </div>
  <h2 class="services__title">SERVICES</h2>
  <div class="rule rule--services"></div>
  <ul class="service-list service-list--left">
    <li>Cremation</li>
    <li>General Removal</li>
  </ul>
  <div class="rule rule--divider"></div>
  <ul class="service-list service-list--right">
    <li>Equine Mortality Services</li>
    <li>Transportation for Necropsy</li>
  </ul>
  <div class="rule rule--lower"></div>
</article>

<article class="card card--cattle">
  <svg class="card__band" viewBox="0 0 700 400" preserveAspectRatio="none" aria-hidden="true">
    <path d="M0,362 L300,362 C330,362 345,368 360,376 L0,376 Z" fill="var(--stripe-grey)"/>
    <path d="M0,376 L300,376 C370,376 380,348 450,348 L700,348 L700,400 L0,400 Z" fill="var(--navy)"/>
  </svg>
  <div class="brand">
    <div class="brand__name"><span class="brand__mark"></span>QRB Farmstock</div>
    <div class="brand__place">Ridgeford, PA</div>
    <div class="brand__phone">555-318-4692</div>
  </div>
  <div class="owner">
    <div class="owner__name">Gerald R. Fenwick</div>
    <div class="owner__title">OWNER</div>
    <div class="owner__rule"></div>
    <ul class="contact">
      <li><svg viewBox="0 0 14 14"><rect x="1" y="3" width="12" height="8" fill="none" stroke="var(--navy)" stroke-width="1.3"/><path d="M1 3 L7 8 L13 3" fill="none" stroke="var(--navy)" stroke-width="1.3"/></svg>info@qrbfarmstockservices.example</li>
      <li><svg viewBox="0 0 14 14"><circle cx="7" cy="7" r="5.5" fill="none" stroke="var(--navy)" stroke-width="1.3"/><path d="M1.5 7 H12.5 M7 1.5 C4 5 4 9 7 12.5 M7 1.5 C10 5 10 9 7 12.5" fill="none" stroke="var(--navy)" stroke-width="1"/></svg>www.QRBFarmstockServices.example</li>
    </ul>
  </div>
  <h2 class="services__title">SERVICES</h2>
  <div class="rule rule--services"></div>
  <ul class="service-list service-list--left">
    <li>Dealing</li>
    <li>Dead Stock Removal</li>
  </ul>
  <div class="rule rule--divider"></div>
  <ul class="service-list service-list--right">
    <li>Hauling, Order Buying</li>
    <li>General Livestock Services</li>
  </ul>
  <div class="rule rule--lower"></div>
</article>

</body>
</html>
```